Brochure for Specialist Divorce Support

1. I want an A4 three fold brochure or DL to promote my business and services.
My market are people going through divorce and are usually feeling very overwhelmed and therefore not functioning very well - both men and women, age early forties,
2. Colours – variety of blues and lime greens but you choose if you need a contrast e.g. orange
3. Images – happy single families
4. Theme - could you make it around water please - soothing
5. Logos – HWN &; HWT (I will attach)
6. I have a lot of content so maybe not too busy but still professional feel +
warm and reassuring
7. I'm attaching -

- a draft brochure I put together using a Microsoft template
- a word document with extra details
- plus two logos to do with my qualifications
- and some images for you to choose from

7. I want to use this as a template for some other brochures -> more work for
the winner.

Target Market(s)

Men and women usually in their early forties with primary school aged children i.e 5 to 12 years old.
They are going through a divorce and very upset, Maybe losing contact with their children and their way of life as they know it is disappearing. They are in turmoil and not functioning as well as they usually do.

Industry/Entity Type

Business

Font styles to use
Sans Serif

Colors
34a7d7
abd037
3277b5

Requirements
Must have
• I want the brochure to be three folds with the center the full A4
• Could you make the theme around water please.
• I will upload some photos for you to use if you want,

```html
<!DOCTYPE html>
<html lang="en">
<head>
<meta charset="utf-8">
<title>Specialist Divorce Support – Brochure</title>
<link href="https://fonts.googleapis.com/css2?family=Roboto+Condensed:ital,wght@0,300;0,400;0,700;1,300;1,400;1,700&family=Kaushan+Script&display=swap" rel="stylesheet">
<style>
:root{
  --sky:#34a7d7;
  --lime:#abd037;
  --ocean:#3277b5;
  --navy:#1f3f6e;
  --ink:#24345a;
  --stage:#1d4b8a;
  --paper:#ffffff;
  --cream:#f6f1e7;
  --backdrop:#1c4f7d;
}
*{box-sizing:border-box;margin:0;padding:0}
html,body{width:1200px;height:1200px;overflow:hidden;background:var(--backdrop)}
body{font-family:"Roboto Condensed",sans-serif;color:var(--ink);position:relative}
.spread{position:absolute;background:var(--paper);display:flex;box-shadow:0 10px 24px rgba(0,0,0,.35)}
.spread--outside{left:219px;top:20px;width:745px;height:577px}
.spread--inside{left:401px;top:610px;width:755px;height:587px}
.panel{position:relative;height:100%;overflow:hidden}

/* outside – benefits panel */
.benefits{width:249px;background:linear-gradient(180deg,#fff 0%,#fff 45%,#d4ebf8 100%)}
.benefits__photo{position:absolute;left:0;top:0;width:249px;height:195px;background:linear-gradient(160deg,#b9d79a 0%,#d9b79c 45%,#eef4f8 100%)}
.benefits__photo::after{content:"";position:absolute;left:0;right:0;bottom:0;height:50px;background:linear-gradient(180deg,rgba(255,255,255,0),#fff)}
.benefits__title{position:absolute;left:22px;top:194px;font-size:21px;font-weight:400;color:var(--stage)}
.benefits__list{position:absolute;left:23px;top:226px;width:212px;list-style:none}
.benefits__list li{font-size:10px;line-height:13px;color:var(--ink);padding:5px 0 6px;border-bottom:1px solid #7f93ad}
.benefits__list li:first-child{padding-top:0}
.benefits__list li:last-child{border-bottom:none}

/* outside – testimonial panel */
.testimonial{width:244px;background:linear-gradient(180deg,#fff 75%,#e6f2fa 100%)}
.testimonial__green{position:absolute;left:0;top:0;width:244px;height:300px;background:var(--lime)}
.testimonial__quote{position:absolute;left:14px;top:42px;width:216px;text-align:center;font-size:9.6px;line-height:13.2px;font-weight:300;color:#1e2d1a}
.testimonial__quote p{margin-bottom:9px}
.testimonial__sign{font-style:italic;font-weight:700}
.testimonial__blue{position:absolute;left:0;top:300px;width:244px;height:167px;background:linear-gradient(180deg,var(--ocean),#4a8dca)}
.testimonial__contact{position:absolute;left:0;top:309px;width:244px;text-align:center;color:#fff}
.testimonial__flex{font-size:11.5px;line-height:15px;font-weight:400}
.testimonial__label{font-size:14px;font-weight:700;margin-top:14px}
.testimonial__link{font-size:14px;font-weight:300}
.testimonial__motto{position:absolute;left:10px;top:482px;width:224px;text-align:center;font-size:12px;line-height:15px;color:#1b2233}
.testimonial__marks{position:absolute;left:30px;top:530px;width:190px;display:flex;justify-content:space-between;align-items:center}
.mark{display:flex;align-items:center;gap:4px;font-size:14px;font-weight:700;color:var(--navy);letter-spacing:1px}
.mark__dot{width:9px;height:9px;border-radius:50%;background:var(--ocean)}

/* outside – cover panel */
.cover{width:252px;background:#fff}
.cover__brand{position:absolute;left:0;top:42px;width:252px;display:flex;justify-content:center;align-items:center}
.cover__brand-name{font-size:36px;font-weight:700;color:var(--navy);letter-spacing:3px}
.cover__line{position:absolute;left:56px;top:83px;width:140px;height:2px;background:var(--navy)}
.cover__title{position:absolute;left:0;top:89px;width:252px;text-align:center;font-weight:700;font-size:23px;line-height:29px;letter-spacing:1px}
.cover__title span{display:block}
.cover__title .t1{color:var(--ocean)}
.cover__title .t2{color:var(--lime)}
.cover__lead{position:absolute;left:20px;top:162px;width:212px;text-align:center;font-size:12px;line-height:15px;color:#121a2a}
.cover__photo{position:absolute;left:0;top:204px;width:252px;height:244px;background:linear-gradient(180deg,#c7e4f5 0%,#5dc4d8 40%,#7ed4d6 55%,#efe3cc 80%,#fbf8f2 100%)}
.cover__script{position:absolute;left:68px;top:212px;width:180px;transform:rotate(-8deg);font-family:"Kaushan Script",cursive;font-size:19px;line-height:22px;color:#fff;text-align:center;text-shadow:0 0 2px var(--ocean),0 0 3px var(--ocean)}
.cover__promise{position:absolute;left:20px;top:462px;width:212px;text-align:center;font-style:italic;font-weight:300;font-size:12px;line-height:15.5px;color:#1d2230}
.cover__url{position:absolute;left:0;top:531px;width:252px;text-align:center;font-size:14.5px;font-weight:700;color:var(--stage)}

/* inside – services & stages */
.stages{width:499px;background:var(--cream)}
.stages__photo{position:absolute;left:0;top:0;width:499px;height:326px;background:linear-gradient(180deg,#eef6fb 0%,#a9cde6 40%,#6fa64a 70%,#8dbd55 100%)}
.stages__photo::after{content:"";position:absolute;left:0;right:0;bottom:0;height:50px;background:linear-gradient(180deg,rgba(246,241,231,0),var(--cream))}
.services__title{position:absolute;left:276px;top:30px;font-size:39px;font-weight:400;color:var(--stage)}
.services__box{position:absolute;left:267px;top:80px;width:212px;height:244px;background:linear-gradient(180deg,rgba(29,75,110,.95),rgba(29,75,110,.78) 85%,rgba(29,75,110,0))}
.services__list{position:absolute;left:277px;top:92px;width:196px;list-style:none;color:#fff}
.services__list li{position:relative;padding-left:11px;font-size:9.6px;line-height:12.3px;margin-bottom:11px}
.services__list li::before{content:"";position:absolute;left:0;top:4px;width:5px;height:5px;border-radius:50%;background:#fff}
.stages__title{position:absolute;left:29px;top:332px;font-size:26px;font-weight:400;color:var(--stage)}
.stage{position:absolute;left:29px;width:452px;font-size:9.6px;line-height:12.2px;color:var(--ink)}
.stage__head{font-size:15px;font-weight:700;color:var(--stage)}
.stage__head small{font-size:9.5px}
.stage--one{top:372px}
.stage--two{top:438px}
.stage--two p{margin-bottom:12px}
.stages__url{position:absolute;left:29px;top:557px;font-size:14.5px;font-weight:700;letter-spacing:6.4px;color:var(--stage)}

/* inside – skills panel */
.skills{width:256px;background:#fff;border-left:3px solid #e4e9ef}
.skills__title{position:absolute;left:11px;top:27px;width:240px;font-size:14.5px;line-height:16px;font-weight:400;color:var(--stage)}
.skills__list{position:absolute;left:9px;top:64px;width:240px;list-style:none}
.skills__list li{position:relative;padding-left:8px;font-size:9.6px;line-height:12.3px;color:var(--ink)}
.skills__list li::before{content:"";position:absolute;left:0;top:4px;width:4px;height:4px;border-radius:50%;background:var(--stage)}
.skills__list li strong{display:block}
.skills__stage{margin:4px 0 1px 6px;font-size:9.6px;line-height:11.5px;font-weight:700;color:var(--stage)}
.skills__stage b{font-size:14.5px}
.skills__photo{position:absolute;left:0;top:430px;width:256px;height:157px;background:linear-gradient(170deg,#fff 0%,#e5edc9 25%,#c5d88e 60%,#d9b89c 100%)}
.skills__pace{position:absolute;right:22px;top:433px;width:130px;text-align:right;font-size:16px;line-height:20px;font-weight:300;color:#1a1f2c}
.skills__pace em{font-weight:700}
</style>
</head>
<body>

<section class="spread spread--outside">
  <div class="panel benefits">
    <div class="benefits__photo" role="img" aria-label="Photo of a smiling mother hugging her young daughter outdoors"></div>
    <h2 class="benefits__title">Coaching can help you:</h2>
    <ul class="benefits__list">
      <li>Save money by being a more collected and credible client in the legal process</li>
      <li>Stay in control and focus on what's important for you and your family to avoid angry, emotional hijacks</li>
      <li>Feel more empowered by being organised and prepared for what's ahead and develop a plan of action</li>
      <li>Identify your next steps re: legal, financial, children's issues plus your self-care</li>
      <li>Develop a draft parenting plan to anticipate and address possible issues</li>
      <li>Consider areas of possible conflict and explore techniques to reduce confrontation</li>
      <li>Find your voice and be more confident in your skills to take control of your divorce and do it your way</li>
      <li>Let go of what was … and create what is possible during your divorce journey and afterwards.</li>
    </ul>
  </div>

  <div class="panel testimonial">
    <div class="testimonial__green"></div>
    <div class="testimonial__quote">
      <p>"After many cups of coffee and long hours of listening to me, my very good friend suggested I speak to Helen, a divorce coach. I was a bit skeptical, especially when a phone session was suggested.</p>
      <p>From my first phone session I felt empowered. It gave me a sense of direction, assisted me to set realistic goals and action plans. Most importantly it aided my self esteem.</p>
      <p>Divorce is overwhelming. Talking to a caring professional like Helen helped me acknowledge my priorities and a way to achieve them. Thank you Helen."<br><span class="testimonial__sign">- Danielle</span></p>
    </div>
    <div class="testimonial__blue"></div>
    <div class="testimonial__contact">
      <p class="testimonial__flex">Coaching works well over the phone,<br>allowing for flexibility of time and<br>place -evening appointments available.</p>
      <p class="testimonial__label">Full details are on:</p>
      <p class="testimonial__link">CalmWatersCoaching.com.au</p>
      <p class="testimonial__label" style="margin-top:2px">or email:</p>
      <p class="testimonial__link">Helen@ShoreSupport.com.au</p>
    </div>
    <p class="testimonial__motto">"Everyone is different and move through these stages at their own pace"</p>
    <div class="testimonial__marks">
      <span class="mark"><span class="mark__dot"></span>HWN</span>
      <span class="mark">HWT</span>
    </div>
  </div>

  <div class="panel cover">
    <div class="cover__brand"><span class="cover__brand-name">HWT</span></div>
    <div class="cover__line"></div>
    <h1 class="cover__title"><span class="t1">SPECIALIST</span><span class="t2">DIVORCE SUPPORT</span></h1>
    <p class="cover__lead">Helping you move through this major life challenge so you can more successfully</p>
    <div class="cover__photo" role="img" aria-label="Photo of a mother walking hand in hand with two young children on a beach by the sea"></div>
    <p class="cover__script">Start living your new life – your way!!</p>
    <p class="cover__promise">Together we will identify your goals, set priorities and develop a plan for tomorrow … moving you through the pain of divorce to regain confidence and start anew.</p>
    <p class="cover__url">CalmWatersCoaching.com.au</p>
  </div>
</section>

<section class="spread spread--inside">
  <div class="panel stages">
    <div class="stages__photo" role="img" aria-label="Photo of a father and son playing soccer on a sunny park lawn"></div>
    <h2 class="services__title">Our Services</h2>
    <div class="services__box"></div>
    <ul class="services__list">
      <li>Specialist divorce support to suit your needs</li>
      <li>Pre-mediation coaching helping you prepare and achieve more positive outcomes to avoid going to court</li>
      <li>Collaborative law coaching to increase crucial skills so you can participate more constructively in negotiations</li>
      <li>Delivery of HWN Conflict Style Profile giving you real feedback on the constructive and destructive behaviours you choose during conflict situations to facilitate more productive discussions</li>
      <li>Corporate Conflict Management Training</li>
    </ul>
    <h2 class="stages__title">You will go through distinct stages:</h2>
    <div class="stage stage--one">
      <p class="stage__head">1. The Preparation Stage <small>– maybe entail one or two coaching sessions</small></p>
      <p>Anticipating all the unknowns and preparing before you see a Family Law Solicitor can save a lot of your solicitor's time and therefore money. The clearer you are on what you want to achieve throughout the process, the more specific legal advice you will receive.</p>
    </div>
    <div class="stage stage--two">
      <p class="stage__head">2. The Business Side of Divorce <small>– maybe two to four coaching sessions</small></p>
      <p>Divorce involves multiple areas of change, intensity of emotions, life changing decisions, loss of family structure and often a sense of isolation not experienced before.</p>
      <p style="margin-bottom:0">The emotional overwhelm associated with relationship breakdown and the associated loss of 24/7 contact with children can impact even the most together person's ability to make well considered decisions.<br>Together, we will process emotions constructively and clarify decisions to be made… for you to be better able to communicate these in negotiations as well as set new boundaries.</p>
    </div>
    <p class="stages__url">CalmWatersCoaching.com.au</p>
  </div>

  <div class="panel skills">
    <h3 class="skills__title">Where necessary we can work on skills you will need for successful outcomes:</h3>
    <ul class="skills__list">
      <li>Conflict resolution skills plus specific verbal &amp; written communication skills important for more neutral emails and messages</li>
      <li>Having difficult conversations</li>
      <li>Preparing before attending joint conferences or mediation</li>
      <li>Managing anger</li>
      <li>Supporting your children to also navigate changed family structures</li>
      <li>Grieving losses … even if you are the one who made the decision to leave</li>
      <li>Strategies for you to start healing and become whole again</li>
      <li>Drafting a parenting plan to anticipate &amp; address possible parenting issues, leading to more positive and successful co-parenting in the long term. <strong>This is in everyone's interests… especially your children's.</strong></li>
      <li>Look at possible stress strategies to sustain your energy levels, important for you to make good considered decisions</li>
      <p class="skills__stage"><b>3. The Moving On Stage</b> – one or two coaching sessions Dealing with endings and focusing on the future:</p>
      <li>Changing your "self" image and building self worth</li>
      <li>Transitioning from married life to being single again</li>
      <li>Address barriers preventing you from moving forward</li>
      <li>Setting realistic goals to help transition to your new life more effectively</li>
    </ul>
    <div class="skills__photo" role="img" aria-label="Photo of a mother and young son lying close together in soft green grass"></div>
    <p class="skills__pace">Everyone is<br><em>different</em> and<br>moves through<br>the stages<br>at their<br><em>own pace.</em></p>
  </div>
</section>

</body>
</html>
```